Business card design for Plumbing and Gas fitting company

We need a business card design for our plumbing and gas fitting company using the company logo and director details. Design should be modern and eye-catching however kept reasonably simple. This design should be targeted at commercial businesses/work so professionalism is key.

Target Market(s)

Commercial/business

Industry/Entity Type

Plumbing

Contact Information for Business Card

Warren Dohey
Director
027 581 9043
warren@vantorplumbingandgas.example
PO Box 7816
Palmerston North 4472

Font styles to use
Sans Serif

Requirements
Must have
• Logo
• Modern
• Kept simple
Nice to have
• Colour scheme based around logo

```html
<!DOCTYPE html>
<html lang="en">
<head>
<meta charset="utf-8">
<title>Vantor Plumbing &amp; Gas — Business Card</title>
<link rel="stylesheet" href="https://fonts.googleapis.com/css2?family=Lato:wght@400;700&display=swap">
<style>
  :root {
    --bg: #1d1d1f;
    --card: #3b3c3f;
    --card-edge: #55575b;
    --blue: #1f8fd0;
    --blue-deep: #15679c;
    --orange: #d9742a;
    --text: #e4e6ea;
    --muted: #b9bcc2;
    --rule: #2a86c2;
  }
  * { box-sizing: border-box; margin: 0; padding: 0; }
  html, body { width: 1200px; height: 1200px; overflow: hidden; background: var(--bg); }
  body { font-family: "Lato", sans-serif; color: var(--text); position: relative; }

  .card {
    position: absolute;
    left: 180px;
    width: 840px;
    height: 480px;
    border-radius: 26px;
    background: var(--card);
    border: 1px solid var(--card-edge);
    overflow: hidden;
  }
  .card--front { top: 90px; }
  .card--back { top: 630px; }

  .brand-panel {
    position: absolute;
    top: 0;
    width: 300px;
    height: 100%;
    background: linear-gradient(160deg, var(--blue) 0%, var(--blue-deep) 100%);
  }
  .card--front .brand-panel { left: 0; border-radius: 0 0 180px 0; }
  .card--back .brand-panel { right: 0; border-radius: 180px 0 0 0; }

  .details {
    position: absolute;
    left: 350px;
    top: 48px;
    right: 40px;
  }
  .logo-lockup {
    display: flex;
    align-items: center;
    gap: 14px;
  }
  .logo-mark {
    width: 52px;
    height: 52px;
    border-radius: 50%;
    background: var(--blue);
    flex: none;
  }
  .company-name {
    font-size: 30px;
    font-weight: 700;
    color: var(--blue);
    white-space: nowrap;
  }
  .divider {
    height: 2px;
    background: var(--rule);
    margin: 20px 0 18px;
    opacity: 0.8;
  }
  .person-name {
    font-size: 38px;
    font-weight: 400;
    color: var(--orange);
    letter-spacing: 1px;
  }
  .person-role {
    font-size: 18px;
    color: var(--muted);
    margin-top: 4px;
  }
  .contact-list { list-style: none; margin-top: 26px; }
  .contact-item {
    display: flex;
    align-items: flex-start;
    gap: 12px;
    font-size: 20px;
    line-height: 1.35;
    margin-bottom: 12px;
    white-space: nowrap;
  }
  .contact-icon { width: 18px; height: 18px; flex: none; margin-top: 4px; fill: var(--orange); }
</style>
</head>
<body>

  <section class="card card--front" aria-label="Business card front">
    <div class="brand-panel"></div>
    <div class="details">
      <div class="logo-lockup">
        <span class="logo-mark" aria-hidden="true"></span>
        <p class="company-name">Vantor Plumbing &amp; Gas</p>
      </div>
      <div class="divider"></div>
      <h1 class="person-name">Warren Dohey</h1>
      <p class="person-role">Director</p>
      <ul class="contact-list">
        <li class="contact-item">
          <svg class="contact-icon" viewBox="0 0 20 20" aria-hidden="true"><path d="M10 2 1 10h3v8h5v-5h2v5h5v-8h3z"/></svg>
          <span>PO Box 7816<br>Palmerston North 4472</span>
        </li>
        <li class="contact-item">
          <svg class="contact-icon" viewBox="0 0 20 20" aria-hidden="true"><path d="M4 2h3l2 5-2 1.5a11 11 0 0 0 4.5 4.5L13 11l5 2v3a2 2 0 0 1-2 2A15 15 0 0 1 2 4a2 2 0 0 1 2-2z"/></svg>
          <span>027 581 9043</span>
        </li>
        <li class="contact-item">
          <svg class="contact-icon" viewBox="0 0 20 20" aria-hidden="true"><path d="M1 4h18v12H1z M2 5l8 6 8-6" stroke="#3b3c3f" stroke-width="1.2"/></svg>
          <span>warren@vantorplumbingandgas.example</span>
        </li>
      </ul>
    </div>
  </section>

  <section class="card card--back" aria-label="Business card back">
    <div class="brand-panel"></div>
  </section>

</body>
</html>
```